THE HOMESTEAD LEDGER
STATIONARY, ENVELOPES, FLYERS, BUSINESS CARDS
Project: THE HOMESTEAD LEDGER
THE HOMESTEAD LEDGER - Real Estate
Creative Brief
Professional
MALCOLM J. VANTREASE
PRINCIPAL BROKER
518 WILLOWCREST DRIVE ELIZABETHTOWN, KENTUCKY 42701
malcolmvantrease@quillmail.example
FRONT SIDE DESIGN AND/OR LOGO WITH INDIVIDUAL INFORMATION AND AREA FOR INDIVIDUAL PICTURE.
AT LEAST "THE HOMESTEAD LEDGER" LOGO. OPEN TO OTHER DESIGN AND/OR BORDERS WITH IT.

```html
<!DOCTYPE html>
<html lang="en">
<head>
<meta charset="utf-8">
<title>The Homestead Ledger — Stationery Set</title>
<link href="https://fonts.googleapis.com/css2?family=Cormorant+Garamond:wght@600&family=Lato:wght@400;700&display=swap" rel="stylesheet">
<style>
  :root {
    --backdrop: #4b3527;
    --paper: #ffffff;
    --olive: #a39b74;
    --olive-light: #cfc9a9;
    --olive-dark: #857d58;
    --rule-grey: #9a9a96;
    --ink: #6d6a5c;
    --ink-soft: #8c8a80;
    --accent: #c8612e;
  }
  * { box-sizing: border-box; margin: 0; padding: 0; }
  html, body { width: 1200px; height: 732px; overflow: hidden; }
  body { background: var(--backdrop); position: relative; font-family: "Lato", sans-serif; }

  .sheet { position: absolute; background: var(--paper); box-shadow: 0 3px 10px rgba(0,0,0,.45); overflow: hidden; }
  .sheet svg.band { position: absolute; inset: 0; width: 100%; height: 100%; }

  .wordmark { position: absolute; font-family: "Cormorant Garamond", serif; font-weight: 600; color: var(--ink); text-align: center; line-height: 1; letter-spacing: .06em; }
  .wordmark .mark-dot { display: block; width: 8px; height: 8px; background: var(--accent); border-radius: 50%; margin: 0 auto 4px; }

  /* Letterhead */
  .letterhead { left: 137px; top: 36px; width: 410px; height: 672px; }
  .letterhead .wordmark { right: 18px; top: 30px; font-size: 15px; width: 120px; }
  .letterhead .watermark { position: absolute; left: 60px; right: 20px; top: 300px; font-family: "Cormorant Garamond", serif; font-weight: 600; color: #e9e9e6; font-size: 46px; line-height: 1; text-align: center; letter-spacing: .04em; }
  .letterhead .contact { position: absolute; left: 132px; bottom: 30px; font-size: 7px; line-height: 1.7; color: var(--ink-soft); letter-spacing: .05em; }

  /* Business cards */
  .card-front { left: 689px; top: 36px; width: 144px; height: 84px; }
  .card-front .portrait { position: absolute; left: 40px; top: 20px; width: 22px; height: 32px; background: linear-gradient(#eeeeea, #d9d7cd); border: 1px solid #fff; }
  .card-front .wordmark { right: 10px; top: 14px; font-size: 7px; width: 62px; }
  .card-front .wordmark .mark-dot { width: 4px; height: 4px; margin-bottom: 2px; }
  .card-front .person { position: absolute; right: 10px; bottom: 12px; font-size: 4px; color: var(--ink-soft); text-align: right; line-height: 1.5; }

  .card-back { left: 838px; top: 113px; width: 146px; height: 79px; background: linear-gradient(160deg, var(--olive-light), var(--olive) 60%, var(--olive-dark)); }
  .card-back .wordmark { left: 0; right: 0; top: 20px; font-size: 9px; color: #f4f2e8; }
  .card-back .wordmark .mark-dot { width: 5px; height: 5px; margin-bottom: 3px; }

  /* Envelopes */
  .envelope-front { left: 607px; top: 211px; width: 454px; height: 202px; }
  .envelope-front .wordmark { left: 36px; top: 72px; font-size: 11px; width: 90px; }
  .envelope-front .contact { position: absolute; left: 40px; top: 122px; font-size: 5px; line-height: 1.7; color: #f0eee4; letter-spacing: .05em; }

  .envelope-back { left: 607px; top: 427px; width: 454px; height: 221px; }
  .envelope-back .wordmark { left: 0; right: 0; top: 28px; font-size: 12px; color: #ebe8d9; }
</style>
</head>
<body>

<section class="sheet letterhead" aria-label="Letterhead">
  <svg class="band" viewBox="0 0 410 672" preserveAspectRatio="none" aria-hidden="true">
    <defs>
      <linearGradient id="lh-olive" x1="0" y1="0" x2="1" y2="1">
        <stop offset="0" stop-color="var(--olive-light)"/>
        <stop offset=".5" stop-color="var(--olive)"/>
        <stop offset="1" stop-color="var(--olive-dark)"/>
      </linearGradient>
    </defs>
    <path d="M0 0 H96 C40 150 22 300 48 430 C68 530 104 600 98 672 H0 Z" fill="url(#lh-olive)"/>
    <path d="M96 0 C40 150 22 300 48 430 C68 530 104 600 98 672" fill="none" stroke="var(--rule-grey)" stroke-width="3"/>
  </svg>
  <div class="wordmark"><span class="mark-dot"></span>THE HOMESTEAD LEDGER</div>
  <div class="watermark">THE HOMESTEAD LEDGER</div>
  <div class="contact">
    518 WILLOWCREST DRIVE<br>
    ELIZABETHTOWN, KENTUCKY 42701<br>
    +1 270 555 0148<br>
    malcolmvantrease@quillmail.example
  </div>
</section>

<section class="sheet card-front" aria-label="Business card front">
  <svg class="band" viewBox="0 0 144 84" preserveAspectRatio="none" aria-hidden="true">
    <path d="M0 0 H66 C78 30 70 60 78 84 H0 Z" fill="var(--olive)"/>
    <path d="M66 0 C78 30 70 60 78 84" fill="none" stroke="var(--rule-grey)" stroke-width="1.2"/>
  </svg>
  <div class="portrait" role="img" aria-label="Area for agent portrait photo"></div>
  <div class="wordmark"><span class="mark-dot"></span>THE HOMESTEAD LEDGER</div>
  <div class="person">MALCOLM J. VANTREASE<br>PRINCIPAL BROKER</div>
</section>

<section class="sheet card-back" aria-label="Business card back">
  <div class="wordmark"><span class="mark-dot"></span>THE HOMESTEAD<br>LEDGER</div>
</section>

<section class="sheet envelope-front" aria-label="Envelope front">
  <svg class="band" viewBox="0 0 454 202" preserveAspectRatio="none" aria-hidden="true">
    <defs>
      <linearGradient id="env-olive" x1="0" y1="0" x2="1" y2="1">
        <stop offset="0" stop-color="var(--olive-light)"/>
        <stop offset=".55" stop-color="var(--olive)"/>
        <stop offset="1" stop-color="var(--olive-dark)"/>
      </linearGradient>
    </defs>
    <path d="M0 0 H150 C126 40 120 80 140 120 C156 150 150 180 142 202 H0 Z" fill="url(#env-olive)"/>
    <path d="M150 0 C126 40 120 80 140 120 C156 150 150 180 142 202" fill="none" stroke="var(--rule-grey)" stroke-width="2"/>
  </svg>
  <div class="wordmark"><span class="mark-dot"></span>THE HOMESTEAD LEDGER</div>
  <div class="contact">
    518 WILLOWCREST DRIVE<br>
    ELIZABETHTOWN, KENTUCKY 42701<br>
    +1 270 555 0148<br>
    malcolmvantrease@quillmail.example
  </div>
</section>

<section class="sheet envelope-back" aria-label="Envelope back">
  <svg class="band" viewBox="0 0 454 221" preserveAspectRatio="none" aria-hidden="true">
    <defs>
      <linearGradient id="flap-olive" x1="0" y1="0" x2="0" y2="1">
        <stop offset="0" stop-color="var(--olive-dark)"/>
        <stop offset="1" stop-color="var(--olive-light)"/>
      </linearGradient>
    </defs>
    <path d="M0 0 H454 V24 C430 40 420 70 400 74 H54 C34 70 24 40 0 24 Z" fill="url(#flap-olive)"/>
    <path d="M0 24 C24 40 34 70 54 74 H400 C420 70 430 40 454 24" fill="none" stroke="var(--rule-grey)" stroke-width="1.5"/>
  </svg>
  <div class="wordmark">THE HOMESTEAD LEDGER</div>
</section>

</body>
</html>
```